New Business Card for Innovative Tool Company

We need a new design of business card for our florida based tool manufacturing company. I will attach 2 files that we use for our logo, use whichever you feel works best for the card. Main colours are as per logo, and we can use different shades of black/white/grey for the background.

Contact Information for Business Card

Name/Jobtitle/cell
Corvalen Tools
Suite 212c
4316 Marrowdale Pkw
Orlando, FL32847
USA
name@corvaleninc.example
www.corvaleninc.example

Font styles to use
Sans Serif

Colors

Designer to choose colors to be used in the design.

Requirements
Must have
• Icons for Plazaro, Chirpet, Snapvale, Findlo & Vidstream

```html
<!DOCTYPE html>
<html lang="en">
<head>
<meta charset="utf-8">
<title>Corvalen Tools – Business Card</title>
<link href="https://fonts.googleapis.com/css2?family=Roboto:wght@400;500;700&family=Roboto+Slab:wght@700&display=swap" rel="stylesheet">
<style>
  :root {
    --backdrop: #2b2b2b;
    --card: #1c1c1d;
    --card-edge: #262627;
    --accent: #f2e51c;
    --text: #f1f1f1;
    --rule: #6a6a6a;
  }
  * { box-sizing: border-box; margin: 0; padding: 0; }
  html, body { width: 1200px; height: 886px; overflow: hidden; }
  body {
    background: var(--backdrop);
    font-family: "Roboto", Arial, sans-serif;
    position: relative;
  }
  .card {
    position: absolute;
    width: 620px;
    height: 354px;
    background: var(--card);
    border: 1px solid var(--card-edge);
    border-radius: 18px;
    box-shadow: 0 14px 30px rgba(0,0,0,.45);
    overflow: hidden;
  }
  .card--back { left: 60px; top: 70px; }
  .card--front { left: 520px; top: 462px; }

  /* shared brand */
  .brand-mark__circle {
    width: 30px; height: 30px;
    border: 2px solid var(--accent);
    border-radius: 50%;
    flex: none;
  }
  .brand-name {
    color: var(--accent);
    font-weight: 700;
    font-size: 40px;
    letter-spacing: 2px;
    text-transform: uppercase;
    white-space: nowrap;
  }

  /* back side */
  .brand-mark {
    position: absolute;
    left: 50%; top: 70px;
    transform: translateX(-50%);
    display: flex; align-items: center; gap: 14px;
  }
  .back-rule {
    position: absolute;
    left: 50px; right: 50px; top: 246px;
    height: 1px;
    background: var(--accent);
    opacity: .55;
  }
  .social-row {
    position: absolute;
    left: 50%; top: 234px;
    transform: translateX(-50%);
    display: flex; gap: 14px;
    background: var(--card);
    padding: 0 14px;
    list-style: none;
  }
  .social-row li {
    display: flex; align-items: center; gap: 5px;
    color: var(--accent);
    font-size: 13px;
    font-weight: 500;
    line-height: 24px;
  }
  .social-row li::before {
    content: "";
    width: 16px; height: 16px;
    border: 1.5px solid var(--accent);
    border-radius: 50%;
  }

  /* front side */
  .front-brand {
    position: absolute;
    left: 0; top: 118px;
    width: 330px;
    display: flex; flex-direction: column; align-items: center; gap: 10px;
  }
  .front-brand .brand-mark__circle { width: 52px; height: 52px; }
  .front-brand .brand-name { font-size: 26px; letter-spacing: 1px; }
  .divider {
    position: absolute;
    left: 330px; top: 70px;
    width: 1px; height: 214px;
    background: var(--rule);
  }
  .contact {
    position: absolute;
    left: 356px; top: 76px;
    color: var(--text);
    font-size: 15.5px;
    line-height: 20px;
  }
  .job-title {
    font-family: "Roboto Slab", Georgia, serif;
    font-weight: 700;
    color: var(--accent);
    font-size: 22px;
    letter-spacing: 1px;
    margin-bottom: 12px;
  }
  .address { font-style: normal; margin-bottom: 10px; }
  .contact-line { display: flex; align-items: center; gap: 10px; }
  .contact-line svg { width: 14px; height: 14px; flex: none; }
</style>
</head>
<body>

<section class="card card--back" aria-label="Card back">
  <div class="brand-mark">
    <span class="brand-mark__circle"></span>
    <span class="brand-name">Corvalen Tools</span>
  </div>
  <div class="back-rule"></div>
  <ul class="social-row">
    <li>Findlo</li>
    <li>Plazaro</li>
    <li>Snapvale</li>
    <li>Chirpet</li>
    <li>Vidstream</li>
  </ul>
</section>

<section class="card card--front" aria-label="Card front">
  <div class="front-brand">
    <span class="brand-mark__circle"></span>
    <span class="brand-name">Corvalen Tools</span>
  </div>
  <div class="divider"></div>
  <div class="contact">
    <h2 class="job-title">JOBTITLE</h2>
    <address class="address">
      Corvalen Tools, Suite 212c<br>
      4316 Marrowdale Pkw<br>
      Orlando, FL32847 USA
    </address>
    <p class="contact-line">
      <svg viewBox="0 0 14 14" aria-hidden="true"><rect x="3" y="1" width="8" height="12" rx="1.5" fill="none" stroke="#f2e51c" stroke-width="1.6"/></svg>
      689 555 0147
    </p>
    <p class="contact-line">
      <svg viewBox="0 0 14 14" aria-hidden="true"><rect x="1" y="3" width="12" height="8" fill="#f2e51c"/><path d="M1 3 L7 8 L13 3" fill="none" stroke="#1c1c1d" stroke-width="1.2"/></svg>
      name@corvaleninc.example
    </p>
    <p class="contact-line">
      <svg viewBox="0 0 14 14" aria-hidden="true"><circle cx="7" cy="7" r="6" fill="#f2e51c"/><path d="M1 7 H13 M7 1 C4 4 4 10 7 13 M7 1 C10 4 10 10 7 13" fill="none" stroke="#1c1c1d" stroke-width="1"/></svg>
      www.corvaleninc.example
    </p>
  </div>
</section>

</body>
</html>
```